Business / Stationery Design Project

Hi,

I need business cards and all other stationary designed for my new finance broking business.

Stationary required:

Business card
Letter head
with compliments
envelopes

There is gold in the logo design so some gold would be good and open to other creative ideas / colours.

Regards
Tomas
Updates

Project Deadline Extended
Reason: Still working through designs.

Target Market(s)

Small to medium business customers. Also to appeal to referrers who include accounting firms and other associated professionals (valuers etc)

Industry/Entity Type

Finance

Requirements
Must have
• Professional, classy look.

```html
<!DOCTYPE html>
<html lang="en">
<head>
<meta charset="utf-8">
<title>Halden Finance – Business Card</title>
<link href="https://fonts.googleapis.com/css2?family=Questrial&display=swap" rel="stylesheet">
<style>
  :root {
    --page-bg: #e9ebec;
    --card-dark: #2a2928;
    --card-dark-hi: #3a3836;
    --card-light: #ffffff;
    --gold: #c9a55a;
    --ink: #1f1f1f;
    --ink-soft: #3a3a3a;
    --shadow: rgba(0, 0, 0, 0.18);
  }
  * { margin: 0; padding: 0; box-sizing: border-box; }
  html, body {
    width: 1200px;
    height: 960px;
    overflow: hidden;
    background: var(--page-bg);
    font-family: "Questrial", "Helvetica Neue", Arial, sans-serif;
  }
  .sheet {
    width: 1200px;
    height: 960px;
    display: flex;
    flex-direction: column;
    align-items: center;
    justify-content: center;
    gap: 40px;
  }
  .card {
    position: relative;
    width: 760px;
    height: 434px;
    box-shadow: 0 10px 30px var(--shadow);
    overflow: hidden;
  }

  /* Front */
  .card-front { background: var(--card-dark); color: #fff; }
  .card-front__pattern {
    position: absolute;
    inset: 0;
    background: linear-gradient(135deg, var(--card-dark-hi) 0%, var(--card-dark) 55%, #232221 100%);
  }
  .card-front__brand {
    position: absolute;
    left: 0; right: 0; top: 178px;
    display: flex;
    align-items: center;
    justify-content: center;
    gap: 16px;
  }
  .brand-dot {
    width: 18px; height: 18px;
    border-radius: 50%;
    background: var(--gold);
  }
  .card-front__name {
    font-size: 46px;
    letter-spacing: 4px;
    text-transform: uppercase;
    color: #ffffff;
  }
  .card-front__web {
    position: absolute;
    left: 0; right: 0; bottom: 30px;
    text-align: center;
    font-size: 22px;
    color: var(--gold);
    letter-spacing: 0.5px;
  }

  /* Back */
  .card-back { background: var(--card-light); color: var(--ink); }
  .card-back__brand {
    position: absolute;
    top: 56px; right: 44px;
    display: flex;
    align-items: center;
    gap: 10px;
  }
  .card-back__brand .brand-dot { width: 12px; height: 12px; }
  .card-back__brand-name {
    font-size: 28px;
    letter-spacing: 2px;
    text-transform: uppercase;
    color: var(--ink-soft);
  }
  .holder {
    position: absolute;
    left: 0; top: 138px;
    display: flex;
    align-items: center;
  }
  .holder__bar {
    width: 12px; height: 38px;
    background: var(--gold);
    margin-right: 16px;
  }
  .holder__name { font-size: 30px; color: var(--ink); letter-spacing: 0.5px; }
  .contacts {
    position: absolute;
    left: 28px; top: 202px;
    list-style: none;
    font-size: 20px;
    line-height: 27px;
    color: var(--ink);
  }
  .contacts__label {
    display: inline-block;
    width: 30px;
    color: var(--gold);
    font-weight: bold;
  }
  .address {
    position: absolute;
    right: 44px; top: 224px;
    font-style: normal;
    text-align: right;
    font-size: 19px;
    line-height: 24px;
    color: var(--ink-soft);
  }
</style>
</head>
<body>
<main class="sheet">
  <section class="card card-front" aria-label="Business card front">
    <div class="card-front__pattern" role="img" aria-label="Dark geometric triangle pattern background"></div>
    <div class="card-front__brand">
      <span class="brand-dot"></span>
      <span class="card-front__name">Halden Finance</span>
    </div>
    <div class="card-front__web">www.haldenfinance.com.au</div>
  </section>

  <section class="card card-back" aria-label="Business card back">
    <div class="card-back__brand">
      <span class="brand-dot"></span>
      <span class="card-back__brand-name">Halden Finance</span>
    </div>
    <div class="holder">
      <span class="holder__bar"></span>
      <span class="holder__name">Greg Tomas</span>
    </div>
    <ul class="contacts">
      <li><span class="contacts__label">P :</span>+61 (0) 2 9555 0142</li>
      <li><span class="contacts__label">F :</span>+61 (0) 2 9555 0187</li>
      <li><span class="contacts__label">M:</span>+61 (0) 400 555 318</li>
      <li><span class="contacts__label">E :</span>greg@halden.com.au</li>
    </ul>
    <address class="address">
      Halden Finance PTY LTD<br>
      U4 / 12 Marlow St<br>
      Westbrook, NSW 2150<br>
      Australia
    </address>
  </section>
</main>
</body>
</html>
```